Need a graphic design for front page of tech blog

Hi,

So I'm looking to start a project of redesigning the front homepage for all of my tech sites. I already have a developer that will code the change, so what I need from someone here is to give me a graphic design, which I can then give to my developers to code.

Currently, I have the plain old boring default list of WordPress posts as the front page, which needs to be replaced with something a little more like a magazine or newspaper style. You can see my four sites here:

https://www.pixel-lantern-notes.com/
https://fixbenchowl.com/
https://quietatticforge.com/
https://www.leapingbyquill.com/

I've attached some screenshots of mobile sites that I like in terms of look and style. Some desktop sites that I like are here (I like some parts more than others, I've attached screenshots of the sections I like):

https://www.marbleknoll.com/
https://www.ferncrate.com/
https://www.bramblecorvids.com/
https://www.rovewithal.com/
https://www.dunecord.com/

Basically, I don't need all that text after each post. Seems like most sites now just have an image, a title, the author and date info and possibly the category.

Right now I'm only showing 10 posts and one has to scroll through lots of text to see them all. The sidebar is good, but I think we can get rid of that for the front page and instead have different sections like Latest Tips, and then some section headers based on the categories.

Anyway, I'm looking for someone who can come up with multiple designs, so that I have some choice.

I'm looking to get this done over the next few weeks. Also, please include in your price the cost of any revisions and how many revisions can be done.

Thanks

Tobrin

```html
<!DOCTYPE html>
<html lang="en">
<head>
<meta charset="utf-8">
<title>Tech Blog – Front Page</title>
<link rel="stylesheet" href="https://fonts.googleapis.com/css2?family=Figtree:wght@400;600;700;800&display=swap">
<style>
:root{
  --orange:#f28c30;
  --navy:#212a36;
  --blue:#1f5fc0;
  --link-blue:#2a64c6;
  --pale-blue:#a8c7ee;
  --text:#4a4f57;
  --muted:#b8c4d4;
  --white:#ffffff;
  --logo-red:#e0463c;
}
*{box-sizing:border-box;margin:0;padding:0}
html,body{width:834px;height:1200px;overflow:hidden;background:var(--white)}
body{position:relative;font-family:"Figtree",sans-serif;color:var(--text)}
.abs{position:absolute}

/* Header */
.site-header{left:0;top:0;width:834px;height:53px;background:var(--white)}
.logo-box{left:89px;top:22px;width:64px;height:20px;border:1px solid var(--logo-red);color:var(--logo-red);font-size:5.5px;display:flex;align-items:center;justify-content:center;letter-spacing:.4px}
.main-nav a{position:absolute;top:27px;font-size:6.5px;color:var(--link-blue);text-decoration:none;letter-spacing:.3px}
.social a{position:absolute;top:25px;width:10px;height:10px;border-radius:50%;background:var(--link-blue)}
.search-bar{left:0;top:53px;width:834px;height:20px;background:var(--orange)}
.search-bar svg{position:absolute;left:702px;top:4px}

/* Hero */
.hero-band{left:0;top:73px;width:834px;height:219px;background:var(--navy)}
.hero-card{left:270px;top:105px;width:294px;height:296px;background:var(--orange)}
.hero-image{width:294px;height:164px;background:linear-gradient(135deg,#cfeaf7 0%,#8fd0ee 55%,#5fb4e0 100%)}
.hero-title{position:absolute;left:31px;top:189px;font-size:9.8px;font-weight:700;color:var(--white);white-space:nowrap}
.hero-more{position:absolute;right:33px;top:189px;color:var(--white);font-size:9px;line-height:1}
.hero-excerpt{position:absolute;left:31px;top:212px;width:218px;font-size:5.5px;line-height:10.4px;color:var(--white)}

/* Tabs */
.tabs{left:121px;top:434px;width:360px;height:14px}
.tab{position:absolute;top:0;font-size:8px;font-weight:700;white-space:nowrap}
.tab-active{left:0;color:var(--link-blue);border-bottom:1px solid var(--link-blue);padding-bottom:1px}
.tab-idle{left:66px;color:var(--pale-blue)}
.tab-rule{position:absolute;left:148px;top:7px;width:211px;height:1px;background:var(--pale-blue)}

/* Post cards */
.post{position:absolute;width:170px}
.post-image{width:170px;height:96px}
.post-title{margin-top:16px;font-size:8.2px;line-height:13px;font-weight:700;color:var(--orange)}
.post-excerpt{margin-top:6px;width:166px;font-size:5.4px;line-height:10.4px;color:var(--text)}
.post-meta{margin-top:7px;display:flex;align-items:center;font-size:5.4px;color:var(--muted);white-space:nowrap}
.post-meta i{display:inline-block;width:7px;height:7px;border-radius:50%;background:var(--link-blue);margin-right:5px}
.post-meta span{margin-right:12px}

/* Sidebar */
.sidebar{left:562px;top:446px;width:151px}
.signup-text{width:116px;font-size:7px;line-height:8.8px;color:var(--link-blue)}
.signup-row{display:flex;gap:9px;margin-top:10px}
.signup-input{width:90px;height:17px;border:1px solid var(--orange)}
.signup-btn{width:52px;height:17px;border:1px solid var(--orange);color:var(--orange);font-size:4.2px;font-weight:700;display:flex;align-items:center;justify-content:center;letter-spacing:.3px}
.featured-heading{margin-top:10px;margin-left:4px;font-size:8px;font-weight:700;color:var(--orange)}
.feature{position:absolute;left:4px;width:148px}
.feature-image{width:148px;height:86px}
.feature-title{margin-top:14px;font-size:7.5px;font-weight:700;color:var(--link-blue)}
.feature-excerpt{margin-top:6px;font-size:5.4px;line-height:10px;color:var(--text)}

/* Footer */
.site-footer{left:0;top:1097px;width:834px;height:103px;background:var(--blue);color:var(--white)}
.footer-heading{position:absolute;left:121px;top:23px;font-size:6px;font-weight:700;white-space:nowrap}
.footer-text{position:absolute;left:121px;top:39px;width:150px;font-size:5.4px;line-height:10.4px}
.footer-input{position:absolute;left:121px;top:65px;width:90px;height:17px;border:1px solid var(--white);font-size:5.4px;padding-left:8px;display:flex;align-items:center}
.footer-btn{position:absolute;left:221px;top:65px;width:52px;height:17px;background:var(--orange);font-size:4.2px;font-weight:700;display:flex;align-items:center;justify-content:center}
.footer-col{position:absolute;top:22px;list-style:none;font-size:4.2px;font-weight:700;line-height:11.2px;letter-spacing:.1px;white-space:nowrap}

/* Image placeholder tones */
.tone-chart{background:linear-gradient(90deg,#f4f6fa 0%,#3f78d8 45%,#5a93e8 60%,#eef2f8 100%)}
.tone-phones{background:linear-gradient(90deg,#b9bcc2 0%,#a9708d 40%,#2a3560 70%,#121520 100%)}
.tone-dark{background:linear-gradient(90deg,#1a1a1c 0%,#3a1414 55%,#a02222 100%)}
.tone-lock{background:linear-gradient(90deg,#9a2f8e 0%,#e34a86 35%,#ea5484 60%,#3a6fc4 80%)}
.tone-forest{background:linear-gradient(160deg,#5b6f55 0%,#2f3b2e 60%,#1f2a20 100%)}
.tone-cartoon{background:linear-gradient(90deg,#f2a24a 0%,#7ec94d 35%,#4fb0e8 65%,#c65cd6 100%)}
.tone-paper{background:linear-gradient(160deg,#b9d3e6 0%,#e9ecef 45%,#d6d9dc 100%)}
.tone-red{background:linear-gradient(90deg,#ffffff 0%,#ffffff 40%,#d62a22 55%,#c8221c 100%)}
</style>
</head>
<body>

<header class="site-header abs">
  <div class="logo-box abs">LOGO</div>
  <nav class="main-nav">
    <a href="#" style="left:198px">WINDOWS</a>
    <a href="#" style="left:267px">TIPS</a>
    <a href="#" style="left:334px">SOFTWARE</a>
    <a href="#" style="left:423px">OTHER</a>
  </nav>
  <div class="social">
    <a href="#" style="left:614px" aria-label="Social link one"></a>
    <a href="#" style="left:644px" aria-label="Social link two"></a>
    <a href="#" style="left:672px" aria-label="Social link three"></a>
    <a href="#" style="left:702px" aria-label="Social link four"></a>
  </div>
</header>

<div class="search-bar abs">
  <svg width="12" height="12" viewBox="0 0 12 12" aria-label="Search">
    <circle cx="5" cy="5" r="3.8" fill="none" stroke="#fff" stroke-width="1.4"/>
    <line x1="7.8" y1="7.8" x2="11" y2="11" stroke="#fff" stroke-width="1.4" stroke-linecap="round"/>
  </svg>
</div>

<div class="hero-band abs"></div>
<article class="hero-card abs">
  <div class="hero-image" role="img" aria-label="Illustration of two desks with laptops and app icons"></div>
  <h1 class="hero-title">Top 10 Collaboration Tools for Remote Teams</h1>
  <span class="hero-more">⋮</span>
  <p class="hero-excerpt">Many companies are allowing their employees to work from remote locations. Organization, coordination, and communication are paramount when it comes to managing a team of employees, especially those working in different time zones. Traditional workers and teams benefit from the body language and non-verbal cues facilitated by face-to-face interactions. Advancing cloud technologies and screen-sharing applications [...]</p>
</article>

<div class="tabs abs">
  <span class="tab tab-active">Latest Posts</span>
  <span class="tab tab-idle">Random Posts</span>
  <span class="tab-rule"></span>
</div>

<main>
  <article class="post" style="left:121px;top:462px">
    <div class="post-image tone-chart" role="img" aria-label="Phone screenshots showing battery usage charts"></div>
    <h2 class="post-title">Excepteur sint occaecat cupidatat non proident sunt in culpa.</h2>
    <p class="post-excerpt">Excepteur sint occaecat cupidatat non proident, sunt in culpa qui officia deserunt mollit anim id est eopksio laborum. Sed ut perspiciatis unde omnis istpoe natus error sit voluptatem.</p>
    <div class="post-meta"><i></i><span>Long Name Here</span><i></i><span>1h ago</span></div>
  </article>
  <article class="post" style="left:307px;top:462px">
    <div class="post-image tone-phones" role="img" aria-label="Row of smartphones in different colours"></div>
    <h2 class="post-title">Excepteur sint occaecat cupidatat non proident sunt in culpa.</h2>
    <p class="post-excerpt">Excepteur sint occaecat cupidatat non proident, sunt in culpa qui officia deserunt mollit anim id est eopksio laborum. Sed ut perspiciatis unde omnis istpoe natus error sit voluptatem.</p>
    <div class="post-meta"><i></i><span>Long Name Here</span><i></i><span>1h ago</span></div>
  </article>

  <article class="post" style="left:121px;top:658px">
    <div class="post-image tone-dark" role="img" aria-label="Dark photo about a data leak warning on a screen"></div>
    <h2 class="post-title">Excepteur sint occaecat cupidatat non proident sunt in culpa.</h2>
    <p class="post-excerpt">Excepteur sint occaecat cupidatat non proident, sunt in culpa qui officia deserunt mollit anim id est eopksio laborum. Sed ut perspiciatis unde omnis istpoe natus error sit voluptatem.</p>
    <div class="post-meta"><i></i><span>Long Name Here</span><i></i><span>1h ago</span></div>
  </article>
  <article class="post" style="left:307px;top:658px">
    <div class="post-image tone-lock" role="img" aria-label="Phone lock screens with fingerprint, PIN and pattern"></div>
    <h2 class="post-title">Excepteur sint occaecat cupidatat non proident sunt in culpa.</h2>
    <p class="post-excerpt">Excepteur sint occaecat cupidatat non proident, sunt in culpa qui officia deserunt mollit anim id est eopksio laborum. Sed ut perspiciatis unde omnis istpoe natus error sit voluptatem.</p>
    <div class="post-meta"><i></i><span>Long Name Here</span><i></i><span>1h ago</span></div>
  </article>

  <article class="post" style="left:121px;top:855px">
    <div class="post-image tone-forest" role="img" aria-label="Browser start page with a clock over a waterfall photo"></div>
    <h2 class="post-title">Excepteur sint occaecat cupidatat non proident sunt in culpa.</h2>
    <p class="post-excerpt">Excepteur sint occaecat cupidatat non proident, sunt in culpa qui officia deserunt mollit anim id est eopksio laborum. Sed ut perspiciatis unde omnis istpoe natus error sit voluptatem.</p>
    <div class="post-meta"><i></i><span>Long Name Here</span><i></i><span>1h ago</span></div>
  </article>
  <article class="post" style="left:307px;top:855px">
    <div class="post-image tone-cartoon" role="img" aria-label="Colourful cartoon show thumbnails"></div>
    <h2 class="post-title">Excepteur sint occaecat cupidatat non proident sunt in culpa.</h2>
    <p class="post-excerpt">Excepteur sint occaecat cupidatat non proident, sunt in culpa qui officia deserunt mollit anim id est eopksio laborum. Sed ut perspiciatis unde omnis istpoe natus error sit voluptatem.</p>
    <div class="post-meta"><i></i><span>Long Name Here</span><i></i><span>1h ago</span></div>
  </article>

  <article class="post" style="left:121px;top:1052px">
    <div class="post-image tone-paper" role="img" aria-label="Hand writing on paper with a pen"></div>
  </article>
  <article class="post" style="left:307px;top:1052px">
    <div class="post-image tone-red" role="img" aria-label="Video platform banner"></div>
  </article>
</main>

<aside class="sidebar abs">
  <p class="signup-text">Excepteur sint occaecat cupidatat non proident, sunt in culpa qui officia</p>
  <div class="signup-row"><div class="signup-input"></div><div class="signup-btn">SUBSCRIBE</div></div>
  <h3 class="featured-heading">Featured Posts</h3>

  <article class="feature" style="top:78px">
    <div class="feature-image tone-lock" role="img" aria-label="Phone lock screens"></div>
    <h4 class="feature-title">Excepteur sint occaecat.</h4>
    <p class="feature-excerpt">Excepteur sint occaecat cupidatat non proident, sunt in culpa qui officia deserunt mollit anim.</p>
  </article>
  <article class="feature" style="top:230px">
    <div class="feature-image tone-chart" role="img" aria-label="Phone battery usage screenshots"></div>
    <h4 class="feature-title">Excepteur sint occaecat.</h4>
    <p class="feature-excerpt">Excepteur sint occaecat cupidatat non proident, sunt in culpa qui officia deserunt mollit anim.</p>
  </article>
  <article class="feature" style="top:382px">
    <div class="feature-image tone-phones" role="img" aria-label="Row of smartphones"></div>
    <h4 class="feature-title">Excepteur sint occaecat.</h4>
    <p class="feature-excerpt">Excepteur sint occaecat cupidatat non proident, sunt in culpa qui officia deserunt mollit anim.</p>
  </article>
  <article class="feature" style="top:534px">
    <div class="feature-image tone-dark" role="img" aria-label="Data leak warning photo"></div>
    <h4 class="feature-title">Excepteur sint occaecat.</h4>
  </article>
</aside>

<footer class="site-footer abs">
  <h5 class="footer-heading">Subscribe to Northpane via Email</h5>
  <p class="footer-text">Excepteur sint occaecat cupidatat non proident, sunt in culpa qui officia</p>
  <div class="footer-input">Email Address</div>
  <div class="footer-btn">SUBSCRIBE</div>
  <ul class="footer-col" style="left:540px">
    <li>+44 300 555 0142</li><li>NORTHPANE@MAIL.COM</li><li>FIND A STORE</li>
  </ul>
  <ul class="footer-col" style="left:600px">
    <li>CONTACT US</li><li>ORDERING &amp; PAYMENT</li><li>SHIPPING</li><li>RETURNS</li><li>FAQ</li><li>SIZING GUIDE</li>
  </ul>
  <ul class="footer-col" style="left:660px">
    <li>ABOUT NORTHPANE KIT</li><li>WORK WITH US</li><li>PRIVACY POLICY</li><li>TERMS &amp; CONDITIONS</li><li>PRESS ENQUIRIES</li>
  </ul>
</footer>

</body>
</html>
```